BRCW Business Cards

Business Cards should contain:
Bright Ridgecrest Coating Works
Felix Darrow
M: 0417 865 093
E: brightRCW@fernpost.example
BRCW logo
TCG logo
Painting & Decorating
Licence # 719362K
slogan: trust the finish of lasting quality

Target Market(s)

all aspect of painting

Industry/Entity Type

Trade

Contact Information for Business Card

Felix Darrow
M: 0417 865 093
E: brightRCW@fernpost.example
BRCW logo
TCG logo
Painting & Decorating
Licence # 719362K

Font styles to use
Serif
Sans Serif

Requirements
Must have
• clear design with nice backround
• two sides
• smal TCG logo
Nice to have
• easy to read
Should not have
• mess
• black
• plastics form

```html
<!DOCTYPE html>
<html lang="en">
<head>
<meta charset="utf-8">
<title>BRCW Business Cards</title>
<link rel="stylesheet" href="https://fonts.googleapis.com/css2?family=Alegreya:wght@500;700&family=Arimo:wght@700&family=Libre+Baskerville:wght@700&family=Italianno&family=Great+Vibes&display=swap">
<style>
  :root {
    --bg: #e9ecec;
    --white: #ffffff;
    --teal: #008f99;
    --teal-dark: #17564f;
    --grey: #8c8c8c;
    --green: #3f8a2c;
    --blue: #2a63b3;
    --orange: #f0551e;
    --ink: #1e3a36;
  }
  * { box-sizing: border-box; margin: 0; padding: 0; }
  html, body { width: 1200px; height: 1200px; overflow: hidden; background: var(--bg); }
  .sheet { position: relative; width: 1200px; height: 1200px; }
  .card {
    position: absolute; left: 100px; width: 1000px; height: 540px;
    background: var(--white); overflow: hidden;
    box-shadow: 0 6px 18px rgba(0,0,0,0.18);
  }
  .card--front { top: 40px; }
  .card--back { top: 620px; }
  .card__shape { position: absolute; inset: 0; }

  .guild-mark {
    position: absolute; display: flex; align-items: center; gap: 8px;
    font-family: "Alegreya", serif; font-weight: 700; color: var(--blue);
  }
  .guild-mark__dot { width: 14px; height: 14px; border-radius: 50%; background: var(--blue); }
  .guild-mark__name { font-size: 22px; letter-spacing: 2px; }
  .guild-mark__sub {
    position: absolute; top: 30px; left: 0; width: 200px;
    font-family: "Arimo", sans-serif; font-size: 9px; font-weight: 700; color: var(--blue); letter-spacing: 0.5px;
  }
  .card--front .guild-mark { left: 160px; top: 60px; }
  .card--back .guild-mark { left: 220px; top: 60px; }

  .brand { position: absolute; display: flex; align-items: stretch; }
  .brand__art {
    width: 100px; height: 180px; border-radius: 10px 10px 40px 40px;
    background: linear-gradient(180deg, #e97a3a 0%, #6cae3c 40%, #17564f 100%);
  }
  .brand__rule { width: 2px; background: var(--teal-dark); margin: 0 18px; }
  .brand__text { display: flex; flex-direction: column; justify-content: center; }
  .brand__initials {
    font-family: "Libre Baskerville", serif; font-weight: 700; color: var(--teal-dark);
    font-size: 70px; line-height: 1; letter-spacing: 2px;
  }
  .brand__line1 { font-family: "Alegreya", serif; font-weight: 700; color: var(--green); font-size: 28px; line-height: 1.2; margin-top: 8px; }
  .brand__line2 { font-family: "Alegreya", serif; font-weight: 700; color: var(--ink); font-size: 30px; line-height: 1.15; }
  .brand__slogan { font-family: "Italianno", cursive; color: var(--green); font-size: 24px; line-height: 1; }
  .brand__licence { font-family: "Arimo", sans-serif; color: var(--blue); font-size: 14px; text-align: right; margin-top: 2px; }

  .card--front .brand { left: 60px; top: 140px; }
  .card--front .brand__text { width: 250px; }
  .card--front .brand__initials { font-size: 58px; }
  .card--front .brand__line1 { font-size: 26px; }
  .card--front .brand__line2 { font-size: 28px; }
  .card--back .brand { left: 50px; top: 180px; }

  .services {
    position: absolute; left: 120px; top: 410px;
    font-family: "Great Vibes", cursive; color: var(--orange); font-size: 40px;
    border-bottom: 2px solid var(--orange); line-height: 1.1;
  }

  .contact { position: absolute; left: 540px; top: 130px; color: var(--white); }
  .contact__name {
    font-family: "Libre Baskerville", serif; font-weight: 700; font-size: 40px; letter-spacing: 1px;
    text-transform: uppercase; border-bottom: 3px solid var(--white); display: inline-block; line-height: 1.1;
  }
  .contact__row { font-family: "Arimo", sans-serif; font-weight: 700; font-size: 28px; margin-top: 26px; }
</style>
</head>
<body>
<main class="sheet">

  <section class="card card--front" aria-label="Card front">
    <svg class="card__shape" viewBox="0 0 1000 540" width="1000" height="540" aria-hidden="true">
      <polygon points="445,0 1000,0 1000,540 560,540 520,370 445,240 480,175" fill="var(--grey)"/>
      <polygon points="475,0 1000,0 1000,540 590,540 550,370 475,250 505,180" fill="var(--teal)"/>
      <circle cx="485" cy="255" r="22" fill="var(--teal)"/>
      <path d="M476 246 q2 -3 5 0 l3 4 q1 2 -1 4 l-2 1 q2 5 7 7 l1 -2 q2 -2 4 -1 l4 3 q3 3 0 5 q-4 4 -9 2 q-10 -5 -14 -15 q-2 -5 2 -8z" fill="var(--white)"/>
      <circle cx="505" cy="325" r="22" fill="var(--teal)"/>
      <rect x="494" y="317" width="22" height="16" fill="var(--white)"/>
      <polyline points="494,317 505,327 516,317" fill="none" stroke="var(--teal)" stroke-width="2"/>
    </svg>

    <div class="guild-mark">
      <span class="guild-mark__dot"></span>
      <span class="guild-mark__name">TCG</span>
      <span class="guild-mark__sub">TRADE COATERS GUILD NSW CHAPTER</span>
    </div>

    <div class="brand">
      <div class="brand__art" role="img" aria-label="Brand illustration: paint brush topped with colourful trees"></div>
      <div class="brand__rule"></div>
      <div class="brand__text">
        <div class="brand__initials">BRCW</div>
        <div class="brand__line1">Bright Ridgecrest</div>
        <div class="brand__line2">Coating Works</div>
        <div class="brand__slogan">trust the finish of lasting quality</div>
        <div class="brand__licence">Licence: 719362K</div>
      </div>
    </div>

    <div class="services">Painting &amp; Decorating</div>

    <div class="contact">
      <div class="contact__name">Felix Darrow</div>
      <div class="contact__row">0417 865 093</div>
      <div class="contact__row">brightRCW@fernpost.example</div>
    </div>
  </section>

  <section class="card card--back" aria-label="Card back">
    <svg class="card__shape" viewBox="0 0 1000 540" width="1000" height="540" aria-hidden="true">
      <polygon points="570,0 1000,0 1000,540 540,540 540,420 575,365 575,0" fill="var(--teal)"/>
    </svg>

    <div class="guild-mark">
      <span class="guild-mark__dot"></span>
      <span class="guild-mark__name">TCG</span>
      <span class="guild-mark__sub">TRADE COATERS GUILD NSW CHAPTER</span>
    </div>

    <div class="brand">
      <div class="brand__art" role="img" aria-label="Brand illustration: paint brush topped with colourful trees"></div>
      <div class="brand__rule"></div>
      <div class="brand__text">
        <div class="brand__initials">BRCW</div>
        <div class="brand__line1">Bright Ridgecrest</div>
        <div class="brand__line2">Coating Works</div>
      </div>
    </div>
  </section>

</main>
</body>
</html>
```